Copperlamp Revue Parlour

I need a poster design for a variety show.
Key words - burlesque, Victorian, magic, juggling, dance, cirque acts, classy, sexy.

MY DEADLINE IS the 16th 2days from now

Target Market(s)

Adults

Industry/Entity Type

Entertainment Industry

Font styles to use
Serif

Colors
9bcb3c

Requirements
Must have
• It should read like this. COPPERLAMP REVUE. Top of poster
• Images. In the middle
• PARLOUR. Bottom of poster
Nice to have
• Can anyone copy a design and simply add our text. If possible
• I’d like to use file #1 below
Should not have
• Naked girls.

```html
<!DOCTYPE html>
<html lang="en">
<head>
<meta charset="utf-8">
<title>Copperlamp Revue Parlour – Variety Show</title>
<link rel="stylesheet" href="https://fonts.googleapis.com/css2?family=Roboto:wght@100;400;900&family=Open+Sans:wght@700&display=swap">
<style>
  :root {
    --lime: #9bcb3c;
    --lime-glow: #cde23a;
    --lime-deep: #7dc242;
    --crowd: #86c545;
    --ink: #233018;
    --white: #ffffff;
  }
  html, body {
    margin: 0;
    padding: 0;
    overflow: hidden;
  }
  .poster {
    position: relative;
    width: 934px;
    height: 1200px;
    overflow: hidden;
    background:
      radial-gradient(ellipse 55% 35% at 50% 66%, rgba(212,230,58,0.85), rgba(212,230,58,0) 70%),
      linear-gradient(100deg, rgba(255,255,255,0) 30%, rgba(230,245,120,0.18) 45%, rgba(255,255,255,0) 60%),
      linear-gradient(180deg, var(--lime) 0%, #a6d13c 50%, var(--lime-deep) 100%);
    color: var(--ink);
    font-family: "Roboto", Arial, sans-serif;
  }
  .crowd {
    position: absolute;
    left: 0;
    top: 750px;
    width: 934px;
    height: 240px;
    background:
      radial-gradient(ellipse 8% 60% at 12% 100%, rgba(120,190,65,0.9), rgba(120,190,65,0) 100%),
      radial-gradient(ellipse 8% 70% at 40% 100%, rgba(120,190,65,0.9), rgba(120,190,65,0) 100%),
      radial-gradient(ellipse 8% 65% at 72% 100%, rgba(120,190,65,0.9), rgba(120,190,65,0) 100%),
      linear-gradient(180deg, rgba(134,197,69,0) 0%, rgba(134,197,69,0.65) 45%, var(--crowd) 100%);
  }
  .ground {
    position: absolute;
    left: 0;
    top: 985px;
    width: 934px;
    height: 215px;
    background: var(--lime-deep);
  }
  .ornaments {
    position: absolute;
    left: 0;
    top: 0;
  }
  .title {
    margin: 0;
    font-weight: inherit;
  }
  .title-line {
    position: absolute;
    left: 0;
    width: 934px;
    padding-left: 46px;
    box-sizing: border-box;
    text-align: center;
    line-height: 1;
    white-space: nowrap;
  }
  .title-line--light {
    top: 304px;
    font-size: 98px;
    font-weight: 100;
  }
  .title-line--heavy {
    top: 398px;
    font-size: 140px;
    font-weight: 900;
  }
  .title-line--spaced {
    top: 530px;
    font-size: 90px;
    font-weight: 900;
    letter-spacing: 0.2em;
    padding-left: 64px;
  }
  .show-banner {
    position: absolute;
    left: 222px;
    top: 624px;
    width: 534px;
    height: 66px;
    background: var(--ink);
    color: var(--white);
    font-size: 50px;
    font-weight: 400;
    letter-spacing: 0.2em;
    line-height: 66px;
    text-align: center;
    text-indent: 0.2em;
  }
  .schedule {
    position: absolute;
    left: 0;
    top: 724px;
    width: 934px;
    padding-left: 40px;
    box-sizing: border-box;
    margin: 0;
    text-align: center;
    font-size: 52px;
    font-weight: 400;
    line-height: 1;
  }
  .details {
    margin: 0;
    padding: 0;
    list-style: none;
    font-family: "Open Sans", Arial, sans-serif;
    font-weight: 700;
    font-size: 14px;
    color: #1c2412;
  }
  .details li {
    position: absolute;
    top: 1127px;
    white-space: nowrap;
  }
  .details .date { left: 42px; }
  .details .venue { left: 202px; }
  .details .phone { left: 474px; }
  .details .note { left: 598px; }
  .details .web { left: 728px; }
</style>
</head>
<body>
<main class="poster">
  <div class="crowd" role="img" aria-label="Silhouette of a cheering crowd with raised hands"></div>
  <div class="ground"></div>

  <svg class="ornaments" width="934" height="1200" viewBox="0 0 934 1200">
    <defs>
      <linearGradient id="fade-right" x1="0" y1="0" x2="1" y2="0">
        <stop offset="0" stop-color="#233018" stop-opacity="0.32"/>
        <stop offset="1" stop-color="#233018" stop-opacity="0"/>
      </linearGradient>
      <linearGradient id="fade-down" x1="0" y1="0" x2="0" y2="1">
        <stop offset="0" stop-color="#233018" stop-opacity="0.32"/>
        <stop offset="1" stop-color="#233018" stop-opacity="0"/>
      </linearGradient>
      <linearGradient id="fade-left" x1="1" y1="0" x2="0" y2="0">
        <stop offset="0" stop-color="#233018" stop-opacity="0.3"/>
        <stop offset="1" stop-color="#233018" stop-opacity="0"/>
      </linearGradient>
      <linearGradient id="fade-up" x1="0" y1="1" x2="0" y2="0">
        <stop offset="0" stop-color="#233018" stop-opacity="0.3"/>
        <stop offset="1" stop-color="#233018" stop-opacity="0"/>
      </linearGradient>
      <radialGradient id="corner-bloom" cx="0.5" cy="0.5" r="0.5">
        <stop offset="0" stop-color="#233018" stop-opacity="0.3"/>
        <stop offset="1" stop-color="#233018" stop-opacity="0"/>
      </radialGradient>
    </defs>

    <g role="img" aria-label="Ornate Victorian scrollwork and floral flourish framing the top-left corner">
      <rect x="50" y="42" width="520" height="62" rx="31" fill="url(#fade-right)"/>
      <rect x="46" y="50" width="64" height="500" rx="32" fill="url(#fade-down)"/>
      <ellipse cx="170" cy="170" rx="180" ry="180" fill="url(#corner-bloom)"/>
      <line x1="112" y1="106" x2="586" y2="106" stroke="var(--ink)" stroke-width="3" stroke-linecap="round"/>
      <line x1="112" y1="104" x2="112" y2="596" stroke="var(--ink)" stroke-width="3" stroke-linecap="round"/>
      <circle cx="60" cy="56" r="8" fill="var(--ink)"/>
    </g>

    <g role="img" aria-label="Ornate Victorian scrollwork framing the bottom-right corner">
      <rect x="790" y="704" width="62" height="390" rx="31" fill="url(#fade-up)"/>
      <rect x="470" y="1030" width="390" height="62" rx="31" fill="url(#fade-left)"/>
      <line x1="783" y1="704" x2="783" y2="1020" stroke="var(--ink)" stroke-width="3" stroke-linecap="round"/>
      <line x1="452" y1="1020" x2="788" y2="1020" stroke="var(--ink)" stroke-width="3" stroke-linecap="round"/>
      <circle cx="840" cy="1082" r="8" fill="var(--ink)"/>
    </g>
  </svg>

  <h1 class="title">
    <span class="title-line title-line--light">COPPERLAMP</span>
    <span class="title-line title-line--heavy">REVUE</span>
    <span class="title-line title-line--spaced">PARLOUR</span>
  </h1>

  <div class="show-banner">VARIETY SHOW</div>
  <p class="schedule">EVERY FRIDAY</p>

  <ul class="details">
    <li class="date">SAT 22.06.2014</li>
    <li class="venue">DUIS AUTEM VEL EUM IRIURE</li>
    <li class="phone">0761588302</li>
    <li class="note">LOREM IPSUM</li>
    <li class="web">www.copperlamp.com</li>
  </ul>
</main>
</body>
</html>
```